Tanzeri Corporate Site Template/Blog Design

Company Info: Tanzeri Mechanics is a San Francisco based start-up and spin-off of Halvorsen Polytechnic Automation Institute. Our mission is to transform the consumer experience through personal robotics technology.

Our first public brand, gizmopals.net (GPN), used these technologies to develop engaging toy and gaming category innovations that enhance the way children play and interact with new technologies.

This assignment is about the Tanzeri Mechanic corporate identity and not about GPN

The company is transitioning to include higher end consumer electronics and personal robotics products lines within the next few years, and we would like to establish a more formal corporate identity. Attached please find a user flow of the design needed, as well as our current logo.

High Res .EPS Link below:

https://tzmech.filecrate.example/shared/static/a27c0e91bd3f45a6c0d1.eps

Design Vision: Tanzeri Mechanics is in search of a simple, clean and easily updateable corporate website with an integrated blog. The company's current public profile is primarily GPN with an emphasis our children's toy lines Wuzzit and Clankeroos. Although you should be aware of these toy sites, please do not let them influence your design. What we are looking for is more of a blend of scientific and cool.

We would like to see a site template and design that is clean and approachable. It also needs to be able to support a CMS platform as we need the ability to allow our marketing team to update and manage content as well as add additional features such as video and ecommerce in the future as the company grows. These designs should also work well with Chatterly and Peepwire.

Attached is an image of our corporate card. The current color scheme is very basic but the design should complement them.

The final design and layout should communicate a sleek, innovative and technologically saavy consumer electronics and personal robotics company. Again, we are a consumer oriented organization but the key audiences for this site will be investors, media, retail and biz dev partners, and potential employees

Target Market(s)

Investors, Biz dev and other partners, retail, Media, employees. Consumers secondary

Industry/Entity Type

Electronics

Requirements
Must have
• The site must have all of the tabs that we have identified in the attached user flow.

The design must be able to support a backend content management system. We currently have an upgraded PageLoft account, and can provide access if needed but will soon transition to our own site. we are open to your recommendations. Our objective is to be able to easily update the content without relying on a developer.

Font should be sleek. And not bubbly.
Nice to have
• Clean site design. Simple layouts. A blend between scientific and cool. Easy to navigate tabs and sub tabs. forward thinking imagery

Should not have
• Nothing complex on the Homepage- should be very simple. No cartoonish robots, bright colors. Little or no use of humans in stock photos. No competative products or copy. Toys should be under product tabs, and not featured on the homepage as in our initial design efforts we felt that the two were aesthetically polarizing. Just to confirm, the Tanzeri Corporate site should serve more as the parent site, and the toy lines should stay under the sub navs on the product page.

```html
<!DOCTYPE html>
<html lang="en">
<head>
<meta charset="utf-8">
<title>Tanzeri Mechanics</title>
<link href="https://fonts.googleapis.com/css2?family=Arimo:wght@400;700&family=Source+Sans+3:wght@400;600&display=swap" rel="stylesheet">
<style>
:root{
  --ink:#222;
  --text:#555;
  --muted:#777;
  --red:#c4161c;
  --dark:#2b2b2b;
  --nav:#3a3a3a;
  --nav-active:#8f8f8f;
  --line:#d9d9d9;
  --panel:#f2f2f2;
  --link:#b5651d;
}
*{box-sizing:border-box;margin:0;padding:0}
html,body{width:903px;height:1200px;overflow:hidden;background:#fff}
body{font-family:"Source Sans 3",Arial,sans-serif;color:var(--text)}
.page{position:relative;width:903px;height:1200px;background:linear-gradient(#fff 0,#f4f4f4 140px,#fff 300px)}
.abs{position:absolute}
.topbar{left:0;top:0;width:903px;height:8px;background:var(--dark)}

.brand{left:28px;top:22px;width:334px;height:100px;border-left:1px solid var(--line);border-right:1px solid var(--line);display:flex;flex-direction:column;justify-content:center;padding-left:16px;font-family:Arimo,Arial,sans-serif;font-weight:700;color:var(--ink)}
.brand .name1{font-size:40px;line-height:40px;letter-spacing:1px}
.brand .name2{font-size:22px;letter-spacing:9px;line-height:28px}

.search{left:707px;top:26px;width:169px;height:21px;border:1px solid #ccc;border-radius:2px;background:#fff;font-size:10px;color:#aaa;padding:4px 10px;box-shadow:inset 0 1px 2px rgba(0,0,0,.08)}
.search svg{position:absolute;right:6px;top:5px}
.callus{right:27px;top:61px;font-size:16px;color:#444}

.mainnav{left:449px;top:98px;height:36px;display:flex;border-radius:3px;overflow:hidden;background:linear-gradient(#555,#222);box-shadow:0 2px 3px rgba(0,0,0,.3)}
.mainnav a{display:flex;align-items:center;justify-content:center;color:#eee;font-size:13px;text-decoration:none;border-right:1px solid #1c1c1c;border-left:1px solid #555}
.mainnav a.active{background:linear-gradient(#b0b0b0,#8a8a8a);color:#222}
.submenu{left:524px;top:137px;width:128px;height:93px;background:rgba(95,95,95,.96);border-radius:3px;padding:9px 14px;z-index:5;box-shadow:0 2px 4px rgba(0,0,0,.3)}
.submenu a{display:block;color:#f2f2f2;font-size:12.5px;line-height:19px;text-decoration:none}

.slider{left:0;top:150px;width:903px;height:340px}
.hero{left:43px;top:163px;width:820px;height:259px;background:linear-gradient(120deg,#d8d8dc 0%,#f4f4f5 45%,#c9cacf 70%,#eeeeef 100%)}
.caption{left:29px;top:337px;width:361px;height:51px;background:rgba(40,40,40,.82);color:#fff;font-size:16px;padding:14px 0 0 25px}
.dots{left:392px;top:441px;display:flex;gap:11px}
.dots span{width:16px;height:16px;border-radius:50%;background:radial-gradient(circle at 40% 35%,#fff,#cfcfcf)}
.dots span.on{background:var(--red)}

.login{left:32px;top:503px;width:242px;height:151px;border:1px solid #bbb;padding:14px 10px;box-shadow:0 0 3px rgba(0,0,0,.1)}
.login h3{font-family:Arimo,Arial,sans-serif;font-size:13px;color:var(--ink);padding:0 4px 8px;border-bottom:1px dotted #999}
.login label{position:absolute;left:14px;font-family:Arimo,Arial,sans-serif;font-size:10px;color:#333}
.login .field{position:absolute;left:82px;width:132px;height:25px;border:1px solid #aaa;border-radius:4px;background:linear-gradient(#e8e8e8,#f6f6f6)}
.login .submit{position:absolute;left:138px;top:117px;width:68px;height:23px;background:var(--red);color:#fff;border-radius:3px;font-family:Arimo,Arial,sans-serif;font-size:10px;text-align:center;line-height:23px}

.photo{left:307px;top:503px;width:217px;height:151px;border:1px solid #ddd;padding:3px;background:#fff}
.photo div{width:100%;height:100%;background:linear-gradient(100deg,#2a2a40,#4a4fb8 40%,#2d2fa0 70%,#3a3a3a)}

.welcome{left:543px;top:505px;width:350px}
.welcome h2{font-family:Arimo,Arial,sans-serif;font-size:16.5px;color:var(--ink);margin-bottom:6px}
.welcome p{font-family:Arimo,Arial,sans-serif;font-size:11.6px;line-height:19px;color:var(--text);padding-left:3px}

.feature{top:716px}
.feature h3{display:flex;align-items:center;gap:6px;font-family:Arimo,Arial,sans-serif;font-weight:400;font-size:18px;color:var(--red);margin-bottom:14px}
.feature p{font-size:12px;line-height:16.5px;text-align:justify;color:var(--text)}
.feature .more{text-align:right;font-family:Arimo,Arial,sans-serif;font-size:11.5px;color:var(--red);margin-top:3px}

.news{left:14px;top:886px;width:558px;height:204px;background:var(--panel);padding:8px 8px}
.news h3{display:flex;align-items:center;gap:7px;font-family:Arimo,Arial,sans-serif;font-weight:400;font-size:15px;color:var(--red);margin-bottom:12px}
.news .item{margin-bottom:15px}
.news .meta{font-size:11px;color:#222;margin-bottom:9px}
.news .meta a{color:var(--link);font-size:12.5px;margin-right:17px}
.news .meta span{margin-right:10px}
.news p{font-size:10.5px;line-height:16px;color:#333}

.links{left:614px;top:904px}
.links h4,.contact h4{font-family:Arimo,Arial,sans-serif;font-weight:400;font-size:12px;color:var(--red);margin-bottom:12px}
.links a{display:block;font-size:10.5px;line-height:18.2px;color:#777;text-decoration:underline}
.divider{left:709px;top:900px;width:1px;height:172px;background:var(--line)}
.contact{left:724px;top:904px;width:130px;font-size:10.5px;color:#777;line-height:14.5px}
.contact p{margin-bottom:14px}

.footer{left:0;top:1107px;width:903px;height:93px;border-top:2px solid #ccc;background:#fff}
.institute{left:26px;top:10px;display:flex;align-items:center;gap:6px;width:140px}
.institute i{width:14px;height:14px;background:#9b1b2a;flex:none}
.institute span{font-family:Arimo,Arial,sans-serif;font-weight:700;font-size:9.5px;line-height:11px;color:#9b1b2a}
.copyright{left:0;width:903px;top:43px;text-align:center;font-family:Arimo,Arial,sans-serif;font-size:11px;color:#222;padding-left:10px}
.social{right:14px;top:30px;display:flex;gap:8px}
.social span{display:flex;align-items:center;gap:3px;font-size:10px;color:#2a5d9a}
.social i{width:12px;height:12px;background:#2a6fb5;border-radius:2px}
</style>
</head>
<body>
<div class="page">
  <div class="abs topbar"></div>

  <div class="abs brand" aria-label="Tanzeri Mechanics">
    <div class="name1">TANZERI</div>
    <div class="name2">MECHANICS</div>
  </div>

  <div class="abs search">Search
    <svg width="10" height="10" viewBox="0 0 10 10"><circle cx="4" cy="4" r="3" fill="none" stroke="#bbb" stroke-width="1.3"/><line x1="6.2" y1="6.2" x2="9" y2="9" stroke="#bbb" stroke-width="1.5"/></svg>
  </div>
  <div class="abs callus">Call Us: (555) 410-2286</div>

  <nav class="abs mainnav">
    <a style="width:78px">Home</a>
    <a class="active" style="width:84px">About Us</a>
    <a style="width:94px">Products</a>
    <a style="width:74px">News</a>
    <a style="width:100px">Contact us</a>
  </nav>
  <div class="abs submenu">
    <a>History</a><a>Vision</a><a>Executive Team</a><a>Partners</a>
  </div>

  <svg class="abs slider" viewBox="0 0 903 340" width="903" height="340">
    <path d="M29 0 H878 V285 Q810 305 720 304 Q560 300 456 324 Q350 300 190 304 Q90 305 29 285 Z" fill="#2e2e2e"/>
  </svg>
  <div class="abs hero" role="img" aria-label="Photo of a white humanoid robot crouching"></div>
  <div class="abs caption">Sed ut perspiciatis unde omnis iste natus error</div>
  <div class="abs dots"><span class="on"></span><span></span><span></span><span></span><span></span></div>

  <div class="abs login">
    <h3>LOG IN</h3>
    <label style="top:63px">User Name :</label>
    <div class="field" style="top:56px"></div>
    <label style="top:100px">Password :</label>
    <div class="field" style="top:94px"></div>
    <div class="submit">SUBMIT</div>
  </div>

  <div class="abs photo"><div role="img" aria-label="Photo of an engineer working on a robot in a lab"></div></div>

  <div class="abs welcome">
    <h2>Welcome to TANZERI MECHANICS</h2>
    <p>Lorem ipsum dolor sit amet, consectetur adipiscing elit. vehicula aliquet justo, vel fermentum nisi feugiat id. Aenean tellus magna, vulputate suscipit suscipit sed, mattis a nunc. Mauris urna dui, dignissim. Lorem ipsum dolor sit amet, consectetur adipiscing elit. Suspendisse vehicula aliquet justo, vel fermentum nisi feugiat id. Aenean tellus magna, vulputate suscipit suscipit sed, mattis a nunc. Mauris urna dui, dignissim.</p>
  </div>

  <section class="abs feature" style="left:23px;width:257px">
    <h3><svg width="28" height="28" viewBox="0 0 28 28"><g fill="#555"><circle cx="14" cy="14" r="9"/><rect x="12" y="1" width="4" height="26"/><rect x="1" y="12" width="26" height="4"/><rect x="12" y="1" width="4" height="26" transform="rotate(45 14 14)"/><rect x="12" y="1" width="4" height="26" transform="rotate(-45 14 14)"/></g><circle cx="14" cy="14" r="4" fill="#fff"/></svg>History</h3>
    <p>Neque porro quisquam est, qui dolorem ipsum quia dolor sit amet, consectetur, adipisci velit, sed quia non numquam eius modi tempora incidunt ut labore et dolore magnam aliquam quaerat.</p>
    <div class="more">read more &raquo;</div>
  </section>

  <section class="abs feature" style="left:321px;width:248px">
    <h3><svg width="30" height="26" viewBox="0 0 30 26"><g fill="#555"><circle cx="19" cy="6" r="5"/><path d="M10 22 Q10 12 19 12 Q28 12 28 22 Z"/><circle cx="10" cy="11" r="5"/><path d="M1 26 Q1 17 10 17 Q19 17 19 26 Z"/></g></svg>Partners</h3>
    <p>Neque porro quisquam est, qui dolorem ipsum quia dolor sit amet, consectetur, adipisci velit, sed quia non numquam eius modi tempora incidunt ut labore et dolore magnam aliquam quaerat.</p>
    <div class="more">read more &raquo;</div>
  </section>

  <section class="abs feature" style="left:612px;width:257px">
    <h3><svg width="28" height="30" viewBox="0 0 28 30"><g fill="#555"><circle cx="14" cy="8" r="7"/><path d="M1 29 Q1 16 14 16 Q27 16 27 29 Z"/></g></svg>About Us</h3>
    <p>Neque porro quisquam est, qui dolorem ipsum quia dolor sit amet, consectetur, adipisci velit, sed quia non numquam eius modi tempora incidunt ut labore et dolore magnam aliquam quaerat.</p>
    <div class="more">read more &raquo;</div>
  </section>

  <section class="abs news">
    <h3><svg width="22" height="22" viewBox="0 0 22 22"><rect width="22" height="22" rx="3" fill="#555"/><circle cx="6" cy="16" r="2" fill="#fff"/><path d="M4 10 A8 8 0 0 1 12 18" stroke="#fff" stroke-width="2" fill="none"/><path d="M4 5 A13 13 0 0 1 17 18" stroke="#fff" stroke-width="2" fill="none"/></svg>Latest News</h3>
    <div class="item">
      <div class="meta"><a>http://newsdesk.example/post5666/item5</a><span>April 3rd, 2012</span><span>9.30 Am</span></div>
      <p>Allam corporis suscipit laboriosam, nisi ut aliquid ex ea commodi consequatur Quis autem vel eum iure reprehenderit qui in No one rejects, dislikes, or avoids pleasure itself.</p>
    </div>
    <div class="item">
      <div class="meta"><a>http://newsdesk.example/post5666/item5</a><span>April 3rd, 2012</span><span>9.30 Am</span></div>
      <p>Allam corporis suscipit laboriosam, nisi ut aliquid ex ea commodi consequatur Quis autem vel eum iure reprehenderit qui in No one rejects, dislikes, or avoids pleasure itself.</p>
    </div>
  </section>

  <div class="abs links">
    <h4>Useful Links</h4>
    <a>Cras et enim</a><a>Etiam vitae mauri</a><a>Fusce quis</a><a>Vivamus eget orci</a>
    <a>Cras et enim</a><a>Etiam vitae mauri</a><a>Fusce quis</a><a>Vivamus eget orci</a>
  </div>
  <div class="abs divider"></div>
  <div class="abs contact">
    <h4>Contact Us</h4>
    <p>Quisque ullamcorper enim aturna interdum</p>
    <p>Tel : 555 301 4478</p>
    <p>Fax : 555 301 4478</p>
    <p>Mail : info@tanzeri.example</p>
  </div>

  <footer class="abs footer">
    <div class="abs institute"><i></i><span>Halvorsen Polytechnic Automation Institute</span></div>
    <div class="abs copyright">Copyright © 2012 Tanzeri &nbsp; All rights reserved</div>
    <div class="abs social">
      <span><i></i>Callnest</span><span><i></i>Chatterly</span><span><i></i>Peepwire</span><span><i></i>Linkfold</span>
    </div>
  </footer>
</div>
</body>
</html>
```